Creative Web Design - Intl Market Research Company

We need an innovative web design for an emerging company into the international market research marketplace.

The company, Velmoran Associates, is a Trade, Investment, and Market Research company. Velmoran offers domestic and international companies increased success in the U.S. marketplace by providing a variety of services. (seen on attached brochure)

The website should be cutting edge and creative while having an easy navigation. The color is not fixed and attached logo is not finalized, feel free to post anything from conservative to progressive options. Keep in mind target customers are domestic and international businesses looking to emerge/improve in the U.S. marketplace.

Additional Company information is located in the attached documentation. The documentation is outdated & winner will have priority standing for our next projects.(logo & document re-design)
Updates

I have received a few e-mail requests and have updated the status to guaranteed payment.

Thanks!

Target Market(s)

Any company, foreign and domestic, looking to introduce their product into the U.S. marketplace.

Industry/Entity Type

Market Research

Requirements
Must have
• Easy Navigation
Should not have
• Too many buttons
Difficult navigation
Excessive Typography

```html
<!DOCTYPE html>
<html lang="en">
<head>
<meta charset="utf-8">
<title>Velmoran Associates — Trade, Investment, and Market Research</title>
<link href="https://fonts.googleapis.com/css2?family=Oswald:wght@500&family=Open+Sans:wght@400;600;700&display=swap" rel="stylesheet">
<style>
:root{
  --blue:#0b5cbf;
  --blue-dark:#07439a;
  --blue-light:#1a74d8;
  --nav:#2a2a2a;
  --ink:#1c1c1c;
  --text:#333;
  --muted:#777;
  --card:#2b2b2b;
  --gold:#e0a91b;
  --footer:#1d1d1d;
  --footer-bottom:#121212;
  --line:#c9c9c9;
}
*{margin:0;padding:0;box-sizing:border-box}
html,body{width:1067px;height:1200px;overflow:hidden}
body{position:relative;background:#fff;font-family:Arial,Helvetica,sans-serif;color:var(--text);font-size:11px}
.abs{position:absolute}

/* nav */
.topnav{left:0;top:0;width:1067px;height:42px;background:linear-gradient(#333,#222);border-bottom:1px solid #111}
.topnav ul{list-style:none;position:absolute;left:123px;top:0;display:flex;height:42px}
.topnav li{font-family:'Open Sans',sans-serif;font-weight:600;font-size:11.5px;color:#fff;letter-spacing:.3px;display:flex;align-items:center;justify-content:center;border-right:1px solid #444;height:42px}
.topnav li.active{background:linear-gradient(var(--blue-light),var(--blue))}

/* header */
.masthead{left:0;top:42px;width:1067px;height:101px;background:linear-gradient(var(--blue-light),var(--blue) 60%,var(--blue-dark));border-bottom:3px solid #3a8ae6}
.brand{left:127px;top:60px;display:flex;align-items:center;gap:12px}
.brand-dot{width:64px;height:64px;border-radius:50%;background:#d8b35a}
.brand-name{font-family:'Open Sans',sans-serif;font-weight:700;font-size:26px;color:#fff;line-height:1}
.tagline{left:269px;top:97px;font-family:'Open Sans',sans-serif;font-size:12px;color:#fff}
.langs{left:715px;top:53px;display:flex;gap:7px}
.langs span{width:27px;height:27px;border-radius:50%;border:2px solid #fff}
.search{left:768px;top:102px;width:174px;height:23px;background:#fff;border:1px solid #9bb;display:flex}
.search span{flex:1;font-size:9px;color:#999;padding:6px 7px}
.search b{width:26px;background:var(--gold);display:flex;align-items:center;justify-content:center}

/* hero */
.hero{left:0;top:146px;width:1067px;height:292px;background:linear-gradient(90deg,#f1f1f1,#f7f7f7);border-bottom:4px solid #cfcfcf}
.hero-art{left:470px;top:146px;width:597px;height:292px;background:radial-gradient(circle at 70% 52%,#2f8ee0 0,#1565b9 16%,#cfe0f0 26%,rgba(236,238,240,0) 45%),linear-gradient(90deg,rgba(240,240,240,0),#e6e8eb 40%,#eef0f2)}
.hero h1{left:126px;top:196px;font-family:'Oswald',sans-serif;font-weight:500;font-size:40px;line-height:40px;color:#111;letter-spacing:.2px}
.thumbs{left:124px;top:380px;display:flex;gap:8px}
.thumbs span{width:88px;height:50px;border:2px solid var(--blue);background:linear-gradient(135deg,#dfe6ee,#7aa8d8)}
.thumbs span:first-child{border-color:#fff;box-shadow:0 0 0 1px #bbb}

/* alerts */
.alerts{left:125px;top:457px;width:817px;height:83px;border:1px solid #ccc;background:linear-gradient(#f6f6f6,#e6e6e6)}
.alerts-label{left:0;top:0;width:123px;height:81px;border-right:1px solid #d0d0d0;display:flex;align-items:center;justify-content:center;text-align:center;font-family:'Open Sans',sans-serif;font-weight:700;font-size:17px;line-height:21px;color:#111}
.alerts-photo{left:139px;top:9px;width:81px;height:63px;border:3px solid #fff;box-shadow:0 0 2px #999;background:linear-gradient(135deg,#e8ecef,#9aa7b0)}
.alerts h3{left:229px;top:8px;font-size:12px;color:var(--blue);font-weight:700}
.alerts p{left:229px;top:28px;width:520px;font-size:10.5px;line-height:16px;color:#333}
.pager{display:flex;gap:1px}
.pager span{width:16px;height:16px;background:#8a8a8a;display:flex;align-items:center;justify-content:center}

/* cards */
.card{top:557px;width:255px;height:226px;background:var(--card);border:3px solid #fff;box-shadow:0 0 3px #bbb}
.card-head{height:34px;background:linear-gradient(var(--blue-light),var(--blue-dark));display:flex;align-items:center;padding-left:8px;gap:9px;font-family:'Open Sans',sans-serif;font-size:18.5px;color:#fff}
.card-head i{width:26px;height:26px;border-radius:50%;background:var(--gold);border:2px solid #fff}
.card-photo{margin:8px auto 0;width:233px;height:93px;border:3px solid #fff}
.card p{color:#ccc;font-size:9.5px;line-height:14px;padding:7px 7px 0}
.card a{display:block;color:var(--gold);font-weight:700;font-size:10.5px;padding:10px 7px 0;text-decoration:none}

/* lists */
.section-title{top:799px;font-family:'Open Sans',sans-serif;font-size:19px;color:var(--blue)}
.list{top:832px;width:252px;list-style:none}
.list li{height:24px;border-bottom:1px dashed var(--line);display:flex;align-items:center;gap:8px;font-size:10.5px;color:#333}
.list li:last-child{border:none}
.list li i{width:13px;height:13px;border-radius:50%;background:#9a9a9a;display:flex;align-items:center;justify-content:center}
.list li.on{color:var(--blue)}
.list li.on i{background:var(--blue)}
.quote{left:404px;top:838px;font-family:Georgia,serif;font-size:60px;color:#ccc;line-height:1}
.testimonial{left:427px;top:866px;width:233px;font-size:10px;line-height:14px;color:#333}
.cite{left:573px;top:968px;font-size:10.5px;color:var(--blue)}

/* footer */
.footer{left:0;top:1016px;width:1067px;height:148px;background:var(--footer)}
.divider{top:1016px;width:1px;height:148px;background:#333}
.foot-title{top:1029px;font-family:'Open Sans',sans-serif;font-size:15px;color:#fff;border-bottom:1px dashed #555;padding-bottom:5px;width:208px}
.links{top:1059px;list-style:none;color:#fff;font-size:10.5px;line-height:17.5px}
.links li::before{content:"› ";font-weight:700}
.signup{left:430px;top:1059px;width:210px;color:#fff;font-size:10.5px;line-height:16px}
.email-box{left:428px;top:1095px;width:205px;height:40px;background:var(--blue);padding:7px 8px;display:flex}
.email-box span{flex:1;background:#fff;font-size:9.5px;color:#999;padding:6px 12px}
.email-box b{width:29px;background:#111;color:#fff;font-size:11px;display:flex;align-items:center;justify-content:center}
.contact{left:735px;top:1059px;width:210px;color:#fff;font-size:10.5px;line-height:16px}
.contact .row{display:flex;align-items:center;gap:8px;margin-top:3px;margin-left:-churn}
.contact .row i{width:12px;height:12px;border-radius:50%;background:#888;margin-left:-3px}
.bottombar{left:0;top:1164px;width:1067px;height:36px;background:var(--footer-bottom)}
.copyright{left:127px;top:1176px;color:#ddd;font-size:10.5px}
.social{left:822px;top:1173px;display:flex;gap:10px}
.social span{width:16px;height:16px;border-radius:2px;background:#3b6fb0}
.social span:nth-child(2){background:#c8402f}
.social span:nth-child(3){background:#2c9ad6}
.social span:nth-child(4){background:#1c76b0}
.social span:nth-child(5){background:#e8761c}
</style>
</head>
<body>

<nav class="abs topnav">
  <ul>
    <li class="active" style="width:65px">HOME</li>
    <li style="width:75px">ABOUT</li>
    <li style="width:87px">SERVICES</li>
    <li style="width:147px">MARKET MATCHING</li>
    <li style="width:130px">INDUSTRY ALERT</li>
    <li style="width:146px">MARKET OVERVIEW</li>
    <li style="width:85px">SOURCES</li>
    <li style="width:88px;border-right:none">CONTACT</li>
  </ul>
</nav>

<header class="abs masthead"></header>
<div class="abs brand"><span class="brand-dot"></span><span class="brand-name" style="margin-top:-22px">Velmoran Associates</span></div>
<div class="abs tagline">Trade, Investment, and Market Research</div>
<div class="abs langs" role="img" aria-label="Language selection flags">
  <span style="background:#c33"></span><span style="background:#2a3f8f"></span><span style="background:#2e8b4a"></span><span style="background:#2c9c3c"></span><span style="background:#d8dce6"></span><span style="background:#d9261c"></span><span style="background:#233c98"></span>
</div>
<div class="abs search"><span>Search here...</span><b><svg width="12" height="12" viewBox="0 0 12 12"><circle cx="5" cy="5" r="3.5" fill="none" stroke="#fff" stroke-width="1.8"/><line x1="7.5" y1="7.5" x2="11" y2="11" stroke="#fff" stroke-width="2"/></svg></b></div>

<section class="abs hero"></section>
<div class="abs hero-art" role="img" aria-label="Glass globe resting on financial charts and data tables"></div>
<h1 class="abs" style="left:126px;top:196px;font-family:'Oswald',sans-serif;font-weight:500;font-size:40px;line-height:40px;color:#111">MEETING YOUR BUSINESS<br>INFORMATION NEEDS<br>ACROSS THE GLOBE.</h1>
<div class="abs thumbs">
  <span role="img" aria-label="Slide thumbnail: globe on charts"></span>
  <span role="img" aria-label="Slide thumbnail: business people silhouettes"></span>
  <span role="img" aria-label="Slide thumbnail: pie chart with pen"></span>
</div>

<section class="abs alerts">
  <div class="abs alerts-label">INDUSTRY<br>ALERTS</div>
  <div class="abs alerts-photo" role="img" aria-label="Business partners shaking hands"></div>
  <h3 class="abs">Lorem ipsum dolor sit amet consectetur</h3>
  <p class="abs">Lorem ipsum dolor sit amet, consectetuer adipiscing elit, sed diam sit nonummy nibh euismod tincidunt ut laoreet dolore magna aliuam erat volutpat. Ut wisi enim ad minim veniam,</p>
  <div class="abs pager" style="left:765px;top:9px"><span><svg width="6" height="8"><path d="M5 0L1 4l4 4" fill="none" stroke="#fff"/></svg></span><span><svg width="6" height="8"><path d="M1 0l4 4-4 4" fill="none" stroke="#fff"/></svg></span></div>
</section>

<article class="abs card" style="left:124px">
  <div class="card-head"><i></i>TRADING</div>
  <div class="card-photo" role="img" aria-label="Businesswoman presenting a chart" style="background:linear-gradient(90deg,#bfe0ee,#e8eef2)"></div>
  <p>Lorem ipsum dolor sit amet, consectetue adipisc elit, sed diam sit nonummy nibh euismod tincidu laoreet dolore magna aliuam....</p>
  <a>READ MORE</a>
</article>
<article class="abs card" style="left:400px">
  <div class="card-head"><i></i>INVESTMENT</div>
  <div class="card-photo" role="img" aria-label="Business team meeting at a table" style="background:linear-gradient(90deg,#d9d6d0,#4a4f58)"></div>
  <p>Lorem ipsum dolor sit amet, consectetue adipisc elit, sed diam sit nonummy nibh euismod tincidu laoreet dolore magna aliuam....</p>
  <a>READ MORE</a>
</article>
<article class="abs card" style="left:686px">
  <div class="card-head"><i></i>MARKET RESEARCH</div>
  <div class="card-photo" role="img" aria-label="Smiling businessman in an office" style="background:linear-gradient(90deg,#dfe4e8,#8eaecb)"></div>
  <p>Lorem ipsum dolor sit amet, consectetue adipisc elit, sed diam sit nonummy nibh euismod tincidu laoreet dolore magna aliuam....</p>
  <a>READ MORE</a>
</article>

<h2 class="abs section-title" style="left:125px">Our Services</h2>
<ul class="abs list" style="left:125px">
  <li><i><svg width="7" height="6"><path d="M1 3l2 2 3-4" fill="none" stroke="#fff" stroke-width="1.4"/></svg></i>Importers</li>
  <li class="on"><i><svg width="7" height="6"><path d="M1 3l2 2 3-4" fill="none" stroke="#fff" stroke-width="1.4"/></svg></i>Agents/Represetatives</li>
  <li><i><svg width="7" height="6"><path d="M1 3l2 2 3-4" fill="none" stroke="#fff" stroke-width="1.4"/></svg></i>Distributors</li>
  <li><i><svg width="7" height="6"><path d="M1 3l2 2 3-4" fill="none" stroke="#fff" stroke-width="1.4"/></svg></i>Manufacturers</li>
  <li><i><svg width="7" height="6"><path d="M1 3l2 2 3-4" fill="none" stroke="#fff" stroke-width="1.4"/></svg></i>Joint Venture Partners</li>
  <li><i><svg width="7" height="6"><path d="M1 3l2 2 3-4" fill="none" stroke="#fff" stroke-width="1.4"/></svg></i>Manufacturing Under license Partners</li>
  <li><i><svg width="7" height="6"><path d="M1 3l2 2 3-4" fill="none" stroke="#fff" stroke-width="1.4"/></svg></i>Investment Partners</li>
</ul>

<h2 class="abs section-title" style="left:406px">Testimonials</h2>
<div class="abs pager" style="left:628px;top:834px"><span><svg width="6" height="8"><path d="M5 0L1 4l4 4" fill="none" stroke="#fff"/></svg></span><span><svg width="6" height="8"><path d="M1 0l4 4-4 4" fill="none" stroke="#fff"/></svg></span></div>
<div class="abs quote">&ldquo;</div>
<p class="abs testimonial">Lorem ipsum dolor sit amet, consectetue adipiscing elit, sed diam sit nonummy nibh euismod tincidu ut laoreet dolore magna aliuam erat volutpat. Ut enim ad minim veniam, quis nostrud exerci t ullamcorper suscipit lobortis nisl ut aliquip ex ea odoonse. Duis autem vel eum iriure dolor in hendrerit in vulputate velit essesd sit amet molestie consequat,</p>
<div class="abs cite">Lorem Ipsum, COO</div>

<h2 class="abs section-title" style="left:686px">Our Sources</h2>
<ul class="abs list" style="left:686px">
  <li><i><svg width="7" height="6"><path d="M1 3l2 2 3-4" fill="none" stroke="#fff" stroke-width="1.4"/></svg></i>On Line Databases</li>
  <li class="on"><i><svg width="7" height="6"><path d="M1 3l2 2 3-4" fill="none" stroke="#fff" stroke-width="1.4"/></svg></i>Cd Rom Databases</li>
  <li><i><svg width="7" height="6"><path d="M1 3l2 2 3-4" fill="none" stroke="#fff" stroke-width="1.4"/></svg></i>Industry Associations</li>
  <li><i><svg width="7" height="6"><path d="M1 3l2 2 3-4" fill="none" stroke="#fff" stroke-width="1.4"/></svg></i>Industry Experts</li>
  <li><i><svg width="7" height="6"><path d="M1 3l2 2 3-4" fill="none" stroke="#fff" stroke-width="1.4"/></svg></i>Government Experts</li>
  <li><i><svg width="7" height="6"><path d="M1 3l2 2 3-4" fill="none" stroke="#fff" stroke-width="1.4"/></svg></i>Government Agencies</li>
  <li><i><svg width="7" height="6"><path d="M1 3l2 2 3-4" fill="none" stroke="#fff" stroke-width="1.4"/></svg></i>Trade Journals</li>
</ul>

<footer class="abs footer"></footer>
<div class="abs divider" style="left:379px"></div>
<div class="abs divider" style="left:684px"></div>

<h3 class="abs foot-title" style="left:124px">QUICK LINKS</h3>
<ul class="abs links" style="left:125px"><li>Home</li><li>About</li><li>Services</li><li>Market Matching</li></ul>
<ul class="abs links" style="left:234px"><li>Industry Alert</li><li>Market Overview</li><li>Sources</li><li>Contact</li></ul>

<h3 class="abs foot-title" style="left:428px">NEWSLETTER SIGNUP</h3>
<p class="abs signup">Sign up our news letter to get latest news &amp; offers!</p>
<div class="abs email-box"><span>Enter Your Email</span><b>GO</b></div>

<h3 class="abs foot-title" style="left:732px">CONTACT US</h3>
<div class="abs contact">
  <div>482 Harborview Lane, Suite C, Larkspur Bay, 90417</div>
  <div style="display:flex;align-items:center;gap:8px;margin:3px 0 0 -1px"><i style="width:12px;height:12px;border-radius:50%;background:#888"></i>+1 (555) 318-2740</div>
  <div style="display:flex;align-items:center;gap:8px;margin:3px 0 0 -1px"><i style="width:12px;height:12px;border-radius:50%;background:#888"></i>+1 (555) 604-4190</div>
  <div style="display:flex;align-items:center;gap:8px;margin:3px 0 0 -1px"><i style="width:12px;height:12px;border-radius:50%;background:#888"></i>info@velmoran-mail.com</div>
</div>

<div class="abs bottombar"></div>
<div class="abs copyright">Copyright © 2013 Velmoran Associates .All Rights Reserved.</div>
<div class="abs social" aria-label="Social links"><span></span><span></span><span></span><span></span><span></span></div>

</body>
</html>
```